Cups in Quiet Bloom webdesign + shopvantix implementation

Hi there!
We are a brand new small company located in central Europe, specializing in handmade coffee and tea mugs - please check www.cupsinquietbloom.example

We are looking for a complete redesign, something easy, nothing complicated.

1. web desing (smooth and easy - homepage,product detail page, etc...)
2. html/css
3. shopvantix platform implementation

Industry/Entity Type

It Company

```html
<!DOCTYPE html>
<html lang="en">
<head>
<meta charset="utf-8">
<title>Cups in Quiet Bloom – Coffee mug with 2 cats</title>
<link rel="stylesheet" href="https://fonts.googleapis.com/css2?family=Alegreya:ital,wght@1,700;1,800&family=Noto+Sans:wght@400;700&display=swap">
<style>
:root{
  --paper:#f2ecdc;
  --paper-line:#e6dcc6;
  --panel:#f7f3ea;
  --panel-head:#efe8da;
  --border:#ddd2bd;
  --orange:#d6532c;
  --orange-dark:#b23f1d;
  --orange-light:#e8754d;
  --link:#d5613b;
  --ink:#2f231b;
  --muted:#7b6a5c;
  --wood:#7b2b12;
  --wood-dark:#5a1c0a;
  --wood-light:#93391b;
  --cream:#f3e9d6;
  --leather:#5b3a2c;
  --badge:#4b4a3c;
  --phone:#d9d3a3;
}
*{box-sizing:border-box;margin:0;padding:0}
html,body{width:925px;height:1200px;overflow:hidden}
body{background:var(--paper);font-family:"Noto Sans",Arial,sans-serif;color:var(--ink)}
.page{position:relative;width:900px;height:1168px;transform:scale(1.02778);transform-origin:0 0;
  background:repeating-linear-gradient(45deg,var(--paper) 0 3px,#efe7d5 3px 4px)}
.abs{position:absolute}
a{color:var(--link)}
.heading{font-family:"Alegreya",Georgia,serif;font-style:italic;font-weight:800}

/* header */
.brand{left:112px;top:38px;font-size:17px;color:var(--leather);letter-spacing:.2px}
.brand-dot{display:inline-block;width:10px;height:10px;border-radius:50%;background:var(--leather);margin-right:6px;vertical-align:1px}
.search{left:376px;top:0;width:148px;height:62px}
.search-field{left:390px;top:8px;width:124px;height:18px;background:#8a6352;border:1px solid #a07767;border-radius:3px;color:#e8d9cc;font-size:8px;padding:4px 6px}
.search-btn{left:435px;top:32px;width:30px;height:30px;border-radius:50%;background:var(--orange);border:2px solid #e9866a}
.round-icon{width:38px;height:38px;border-radius:50%;background:#e3dac8;border:2px solid #fff;box-shadow:0 1px 3px rgba(0,0,0,.25)}
.head-link{font-size:9px;text-decoration:underline}

/* nav */
.nav{left:95px;top:70px;width:711px;height:40px;background:linear-gradient(var(--orange-light),var(--orange));border-radius:14px 14px 18px 18px;box-shadow:0 4px 6px rgba(0,0,0,.2)}
.nav ul{list-style:none;display:flex;position:absolute;top:13px;left:27px}
.nav li{color:#fff;font-size:9.5px;text-transform:uppercase;letter-spacing:.2px}

/* panels */
.panel{background:var(--panel);border:1px solid var(--border);box-shadow:0 1px 2px rgba(0,0,0,.08)}
.panel-head{height:28px;background:var(--panel-head);border-bottom:1px solid var(--border);display:flex;align-items:center;padding-left:24px;font-size:13px;position:relative}
.toggle{position:absolute;left:3px;top:6px;width:15px;height:15px;border-radius:50%;background:#fff;border:1px solid var(--border)}
.cat-list{list-style:none}
.cat-list li{height:27.4px;line-height:27px;padding-left:8px;font-size:9px;color:var(--link);border-bottom:1px solid var(--border)}
.cat-list li.current{color:var(--ink);background:#e6dfd1;border-left:3px solid var(--orange);padding-left:5px}
.review{display:flex;height:53px;padding:4px 4px;border-bottom:1px solid var(--border)}
.thumb{width:38px;height:38px;border:2px solid #fff;box-shadow:0 0 2px rgba(0,0,0,.3);background:linear-gradient(#cdc4b8,#a38e7c);flex:none}
.review-text{margin-left:7px;font-size:8.5px;color:var(--link);line-height:12px}
.review-date{color:var(--muted);font-size:8px;margin-top:2px}
.tags{display:flex;flex-wrap:wrap;gap:5px 6px;padding:6px 2px 0}
.tag{font-size:7.5px;padding:3px 5px;background:#e9e1d0;border:1px solid var(--border);color:var(--ink)}

/* main */
.crumbs{left:278px;top:133px;width:528px;height:28px;display:flex;align-items:center;font-size:8.5px}
.crumb-home{width:30px;height:27px;border-right:1px solid var(--border);margin-right:16px}
.photo{left:278px;top:176px;width:244px;height:242px;padding:4px;background:#fff;border:1px solid var(--border)}
.photo-fill{width:100%;height:100%;background:linear-gradient(180deg,#7d7b78 0%,#a59d93 55%,#b59c7a 70%,#8f7558 100%)}
.thumbs{left:281px;top:432px;display:flex;gap:5px}
.thumbs .thumb{width:55px;height:56px}
.title{left:532px;top:176px;font-size:12.5px}
.price{left:532px;top:199px;background:var(--orange);color:#fff;font-weight:700;font-size:11px;padding:2px 5px}
.summary{left:532px;top:225px;width:272px;font-size:8.5px;line-height:13px}
.category{left:532px;top:319px;font-size:7.5px;color:var(--muted)}
.qty{left:532px;top:346px;width:48px;height:23px;background:#e5dccb;border:1px solid var(--border);font-size:8px;text-align:right;padding:6px 4px}
.cart-btn{left:588px;top:346px;width:63px;height:23px;background:var(--orange);color:#fff;font-size:8.5px;text-align:center;line-height:23px;border-radius:2px}
.share{top:388px;display:flex;gap:3px;font-size:7px}
.share-btn{border:1px solid #c9c0ad;background:#f8f6f0;padding:1px 4px;border-radius:2px;font-weight:700;color:#3b4b6a}
.share-count{border:1px solid #c9c0ad;background:#fff;padding:1px 4px}
.tabs{left:278px;top:509px;width:528px;height:29px;background:linear-gradient(var(--orange-light),var(--orange));border-radius:3px;display:flex;align-items:flex-end;padding-left:4px;gap:2px}
.tab{color:#fff;font-size:8.5px;text-transform:uppercase;padding:7px 9px 8px}
.tab.active{background:#fff;color:var(--ink);border-radius:3px 3px 0 0;margin-bottom:3px;padding:6px 9px}
.description{left:288px;top:550px;width:510px;font-size:8.6px;line-height:13.2px}
.description p{margin-bottom:13px}

/* footer */
.footer{left:0;top:900px;width:900px;height:268px;background:linear-gradient(90deg,var(--wood-dark),var(--wood) 20%,var(--wood-light) 50%,var(--wood) 80%,var(--wood-dark));box-shadow:inset 0 3px 6px rgba(0,0,0,.4)}
.help{left:312px;top:866px;width:278px;height:68px}
.help-text{left:368px;top:880px;color:#fff;font-size:11.5px}
.help-phone{left:407px;top:897px;color:var(--phone);font-size:17px;font-weight:700;letter-spacing:.5px}
.help-avatar{left:318px;top:880px;width:42px;height:42px;border-radius:50%;background:#3e3c30;border:2px solid #6f6c5a}
.foot-head{color:#e9c9a9;font-size:12.5px}
.socials{left:95px;top:983px;display:flex;gap:10px}
.social{width:28px;height:28px;border-radius:50%;background:#6b230e;border:1px solid #a54a2a}
.foot-text{color:var(--cream);font-size:8.6px;line-height:12.6px}
.email{left:95px;top:1112px;width:141px;height:22px;background:#5f1e0b;border:1px solid #a4492a;color:#cfa78b;font-size:8px;font-style:italic;padding:5px 6px}
.signup{left:240px;top:1111px;width:78px;height:24px;background:var(--orange);color:#fff;font-size:10px;font-weight:700;padding-left:32px;line-height:24px;border-radius:2px}
.signup-icon{position:absolute;left:0;top:0;width:26px;height:24px;background:var(--orange-dark)}
.quick{left:569px;top:983px;list-style:none}
.quick li{color:var(--cream);font-size:8.6px;height:21.4px;display:flex;align-items:center}
.quick li::before{content:"";width:11px;height:11px;border-radius:50%;background:#4c1708;margin-right:7px;box-shadow:inset 0 0 0 1px #8f3a1e}
</style>
</head>
<body>
<div class="page">

  <!-- header -->
  <div class="abs brand"><span class="brand-dot"></span>Cups in Quiet Bloom</div>

  <svg class="abs search" viewBox="0 0 148 62" aria-hidden="true">
    <path d="M0 0 H148 V38 Q148 44 140 47 L80 60 Q74 62 68 60 L8 47 Q0 44 0 38 Z" fill="#5b3a2c"/>
    <path d="M4 0 V37 Q4 41 10 43 L70 56 Q74 57 78 56 L138 43 Q144 41 144 37 V0" fill="none" stroke="#8f6a58" stroke-dasharray="2 2"/>
  </svg>
  <div class="abs search-field">I am looking for...</div>
  <div class="abs search-btn">
    <svg width="26" height="26" viewBox="0 0 26 26" aria-hidden="true"><circle cx="12" cy="12" r="5" fill="none" stroke="#fff" stroke-width="2"/><line x1="15.5" y1="15.5" x2="19" y2="19" stroke="#fff" stroke-width="2.5" stroke-linecap="round"/></svg>
  </div>

  <div class="abs round-icon" style="left:633px;top:16px">
    <svg width="34" height="34" viewBox="0 0 34 34" aria-hidden="true"><path d="M9 11 H12 L15 21 H24 L26 14 H13" fill="none" stroke="#8a8580" stroke-width="1.5"/><circle cx="16" cy="24" r="1.5" fill="#8a8580"/><circle cx="23" cy="24" r="1.5" fill="#8a8580"/></svg>
  </div>
  <a class="abs head-link" style="left:674px;top:30px">(0) Items</a>
  <div class="abs round-icon" style="left:727px;top:16px">
    <svg width="34" height="34" viewBox="0 0 34 34" aria-hidden="true"><circle cx="17" cy="13" r="5" fill="#c4572f"/><path d="M8 28 Q17 16 26 28 Z" fill="#c4572f"/></svg>
  </div>
  <a class="abs head-link" style="left:768px;top:30px">My Profile</a>

  <nav class="abs nav">
    <ul>
      <li style="width:99px">Homepage</li>
      <li style="width:104px">Categories</li>
      <li style="width:113px">New Arrivals</li>
      <li style="width:117px">About our Mugs</li>
      <li style="width:96px">My Account</li>
      <li>Contact us</li>
    </ul>
  </nav>

  <!-- sidebar -->
  <aside>
    <section class="abs panel" style="left:95px;top:133px;width:170px;height:196px">
      <h3 class="panel-head heading"><span class="toggle"></span>Categories</h3>
      <ul class="cat-list">
        <li>Animal</li>
        <li class="current">Coffee Bean</li>
        <li>Daisies</li>
        <li>Hearts</li>
        <li>Meadow Flowers</li>
        <li style="border-bottom:0">Sun and Clouds</li>
      </ul>
    </section>

    <section class="abs panel" style="left:95px;top:344px;width:170px;height:192px">
      <h3 class="panel-head heading"><span class="toggle"></span>Recent Product Reviews</h3>
      <div class="review"><div class="thumb" role="img" aria-label="Cat mug thumbnail"></div><div class="review-text">Donec luctus dignissim ante nec gravida<div class="review-date">▣ 12 Dec</div></div></div>
      <div class="review"><div class="thumb" role="img" aria-label="Cat mug thumbnail"></div><div class="review-text">Donec luctus dignissim ante nec gravida<div class="review-date">▣ 12 Dec</div></div></div>
      <div class="review" style="border-bottom:0"><div class="thumb" role="img" aria-label="Cat mug thumbnail"></div><div class="review-text">Donec luctus dignissim ante nec gravida<div class="review-date">▣ 12 Dec</div></div></div>
    </section>

    <section class="abs" style="left:95px;top:552px;width:170px">
      <h3 class="panel-head heading panel" style="height:27px"><span class="toggle"></span>Tag Cloud</h3>
      <div class="tags">
        <span class="tag">cool</span><span class="tag">beauty</span><span class="tag">UI</span><span class="tag">luxurious</span>
        <span class="tag">romantic</span><span class="tag">ShopForge</span><span class="tag">web design</span><span class="tag">kiln</span>
      </div>
    </section>
  </aside>

  <!-- product -->
  <div class="abs panel crumbs">
    <span class="crumb-home"><svg width="30" height="27" viewBox="0 0 30 27" aria-hidden="true"><path d="M10 14 L15 9 L20 14 V19 H10 Z" fill="#6b5a4c"/></svg></span>
    <a style="font-style:italic">Online Store</a><span style="margin:0 10px;color:#bbb">›</span><span style="font-style:italic">Product Details</span>
  </div>

  <div class="abs photo"><div class="photo-fill" role="img" aria-label="Handmade clay mug painted with two cats, on a woven mat"></div></div>
  <div class="abs thumbs">
    <div class="thumb" role="img" aria-label="Cat mug view 1"></div>
    <div class="thumb" role="img" aria-label="Cat mug view 2"></div>
    <div class="thumb" role="img" aria-label="Cat mug view 3"></div>
    <div class="thumb" role="img" aria-label="Cat mug view 4"></div>
  </div>

  <h1 class="abs title heading">Coffee mug with 2 cats</h1>
  <div class="abs price">$24.00</div>
  <p class="abs summary">We just love cats and we can't help it! And like any other "cat lover" we enjoy being surrounded by them everywhere. Just imagine your favorite coffee in a mug with two cats smiling at you. This might be just the one you are looking for! We recommend this unique coffee cup as a perfect gift idea for all people that love cats. Raw baked clay outside, brown glaze inside – this coffee mug is all food and dishwasher safe!</p>
  <div class="abs category">Category: <a>Animal</a>, <a>Daisies</a></div>
  <div class="abs qty">1</div>
  <div class="abs cart-btn">Add to Cart</div>
  <div class="abs share" style="left:532px"><span class="share-btn">Share</span><span class="share-count">0</span></div>
  <div class="abs share" style="left:591px"><span class="share-btn">Post</span><span class="share-count">0</span></div>
  <div class="abs share" style="left:666px"><span class="share-btn">Like</span><span class="share-count">0</span></div>

  <div class="abs tabs">
    <span class="tab active">Description</span><span class="tab">Additional Info</span><span class="tab">Comments</span>
  </div>

  <div class="abs description">
    <p>We just love cats and we can't help it! And like any other "cat lover" we enjoy being surrounded by them everywhere. Just imagine your favorite coffee in a mug with two cats smiling at you. This might be just the one you are looking for! We recommend this unique coffee cup as a perfect gift idea for all people that love cats. Raw baked clay outside, brown glaze inside – this coffee mug is all food and dishwasher safe!</p>
    <p>APPROXIMATE MEASURES: Height: 3.1 in / 8 cm In diameter: 3.5 in / 9 cm Capacity: 10.1 oz / 3 dcl</p>
    <p>FEEL OF THE MUG: Handles of our mugs and the spot where the lips touch the mugs are made of a baked clay. Some people need a little time to get used to this feeling. The clay feels just a little bit rough, but it is a matter of time and habit. Actually this is what makes the mugs special - different drinking experience. The motifs are glazed and you can feel the contours. The inside of the mug is glazed and absolutely smooth.</p>
    <p>Symbolic Meaning of Cats As an ancient symbolic Celtic animal, the cat represents the guardian of the Otherworld (or Underworld, depending which texts you read from various regions). In Ancient Romethe cat was sacred to Diana, the moon goddess. Here the cat was also considered a guardian of homes and a symbol of domestic goodness. In Muslimlore, the cat is honored for saving Mohammad from an attack by a fierce snake. Here it is believed the "M" marking on the forehead of many tabby cats is the mark of the prophet ("M" for Mohammad). In Norselegend the cat is depicted drawing the chariot of their fertility goddess, Freyja, and therefore the cat is thought of as a blessing upon newborns and a good omen for those increasing their family ranks. In ancient Egyptcats were sacred and were even depicted on the head of their lunar goddess, Bastet which was worshipped by the ancient Egyptians. In her honor, cats were even mummified along with mice for them to eat.</p>
  </div>

  <!-- footer -->
  <footer class="abs footer"></footer>
  <svg class="abs help" viewBox="0 0 278 68" aria-hidden="true">
    <path d="M14 0 H264 L278 34 L264 68 H14 L0 34 Z" fill="#4b4a3c"/>
    <path d="M18 4 H260 L272 34 L260 64 H18 L6 34 Z" fill="none" stroke="#76745f" stroke-dasharray="2 2"/>
  </svg>
  <div class="abs help-avatar" role="img" aria-label="Support agent avatar"></div>
  <div class="abs help-text heading">Need help with your order? Call us.</div>
  <div class="abs help-phone heading">1 700 555 0142</div>

  <h4 class="abs foot-head heading" style="left:95px;top:957px">Social Profiles</h4>
  <div class="abs socials">
    <span class="social"></span><span class="social"></span><span class="social"></span>
    <span class="social"></span><span class="social"></span><span class="social"></span>
  </div>

  <h4 class="abs foot-head heading" style="left:95px;top:1040px">Newsletter Sign Up</h4>
  <p class="abs foot-text" style="left:95px;top:1066px;width:215px">Lorem ipsum dolor amet, consectetur adipsing. Phasellus efend, enim non euismod lacinia, urna odio convallis.</p>
  <div class="abs email">Enter your e-mail...</div>
  <div class="abs signup"><span class="signup-icon"><svg width="26" height="24" viewBox="0 0 26 24" aria-hidden="true"><rect x="7" y="8" width="12" height="8" fill="none" stroke="#fff"/><path d="M7 8 L13 13 L19 8" fill="none" stroke="#fff"/></svg></span>Sign Up</div>

  <h4 class="abs foot-head heading" style="left:332px;top:957px">Text Example</h4>
  <div class="abs foot-text" style="left:332px;top:983px;width:228px">
    <p style="margin-bottom:12px">Lorem ipsum dolor amet, consectetur adipsing. Phasellus efend, enim non euismod lacinia, urna odio convallis, Comodo mi non orci. Nullam eu sapien ipsum.</p>
    <p style="margin-bottom:12px">Donec luctus dignissim ante nec gravida. Vestibulum sit amet augue leo. Vivamus facilisis sapien eu neque dignissim non vulputate metus facilisis.</p>
    <p>Phasellus pulvinar erat, a magna accumsan vitae. Donec non erat. Sed egestas dolor sed quam facilisis sed molestie fringilla.</p>
  </div>

  <h4 class="abs foot-head heading" style="left:569px;top:957px">Quick Navigation</h4>
  <ul class="abs quick">
    <li>Read more about us</li>
    <li>Customer support 365/24/7</li>
    <li>Shipping information &amp; transport costs</li>
    <li>Terms and conditions</li>
    <li>Legal notice</li>
    <li>Return policy</li>
    <li>Frequently asked questions</li>
  </ul>

</div>
</body>
</html>
```